I need a business card/logo designed that obviously describes my business. We are a residential appraisal and home inspection company in Springfield, MO. We offer residential appraisals, home inspection, pest inspection and radon gas measurement. We have been in business for 18 years and hold state certified residential appraisal licenses and DRUMI certified home inspection licenses. I have a logo that I really like and will attach, but would be open to new suggestions. I like more modern designs than traditional and would like a two sided card with our services, licenses and qualifications on the back.

```html
<!DOCTYPE html>
<html lang="en">
<head>
<meta charset="utf-8">
<title>Larkvale Dwelling Review – Business Card</title>
<link rel="stylesheet" href="https://fonts.googleapis.com/css2?family=Lato:wght@400;700&display=swap">
<style>
  :root {
    --canvas: #2b2b2d;
    --card-white: #fbfbfa;
    --gold: #9b7643;
    --gold-dark: #84622f;
    --orange: #e8870f;
    --brown: #6f5234;
    --ink: #1e1e1e;
    --white: #ffffff;
  }
  * { box-sizing: border-box; margin: 0; padding: 0; }
  html, body {
    width: 1200px; height: 997px; overflow: hidden;
    background: var(--canvas);
    font-family: "Lato", sans-serif;
  }
  .sheet {
    position: relative; width: 1200px; height: 997px;
    display: flex; flex-direction: column; align-items: center; justify-content: center; gap: 60px;
  }
  .card {
    position: relative; width: 700px; height: 400px;
    box-shadow: 0 14px 30px rgba(0,0,0,.45);
  }

  /* Back side */
  .card--back {
    background: linear-gradient(160deg, var(--gold) 0%, var(--gold-dark) 100%);
    color: var(--white);
  }
  .card--back .brand {
    position: absolute; left: 0; right: 0; top: 140px; text-align: center;
  }
  .brand-name {
    display: inline-flex; align-items: center; gap: 12px;
    font-weight: 700; font-size: 40px; letter-spacing: .5px;
  }
  .brand-dot { width: 16px; height: 16px; border-radius: 50%; background: currentColor; }
  .services {
    position: absolute; left: 0; right: 0; top: 222px; text-align: center;
    font-size: 20px; line-height: 1.45;
  }

  /* Front side */
  .card--front { background: var(--card-white); color: var(--ink); }
  .card--front .brand {
    position: absolute; left: 0; right: 0; top: 46px; text-align: center; color: var(--brown);
  }
  .card--front .brand-name { font-size: 36px; }
  .holder {
    position: absolute; right: 40px; top: 140px; text-align: right;
  }
  .holder-name { color: var(--orange); font-weight: 700; font-size: 24px; }
  .holder-title { font-size: 18px; margin-top: 2px; }
  .rule {
    position: absolute; left: 40px; top: 204px; width: 370px; height: 2px; background: var(--orange);
  }
  .contacts {
    position: absolute; left: 40px; top: 250px; list-style: none;
    border-top: 2px solid var(--orange); padding-top: 12px; width: 280px;
  }
  .contacts li {
    display: flex; align-items: center; gap: 14px; font-size: 17px; height: 28px; white-space: nowrap;
  }
  .contacts svg { width: 18px; height: 18px; fill: var(--brown); flex: none; }
  .credential {
    position: absolute; right: 60px; bottom: 50px; text-align: center;
  }
  .credential-seal {
    width: 84px; height: 84px; border-radius: 50%; margin: 0 auto 8px;
    background: radial-gradient(circle at 40% 35%, #e7cf78, #b8922e);
    border: 3px solid #8d6c20;
  }
  .credential-text { color: var(--brown); font-size: 18px; }
</style>
</head>
<body>
<main class="sheet">

  <section class="card card--back" aria-label="Card back">
    <div class="brand"><span class="brand-name"><span class="brand-dot"></span>Larkvale Dwelling Review</span></div>
    <p class="services">Residential Appraisals, Home Inspection,<br>Pest Inspection and Radon Gas Measurement</p>
  </section>

  <section class="card card--front" aria-label="Card front">
    <div class="brand"><span class="brand-name"><span class="brand-dot"></span>Larkvale Dwelling Review</span></div>

    <div class="holder">
      <p class="holder-name">Miles Hartwell</p>
      <p class="holder-title">Project Manager/Estimator</p>
    </div>
    <div class="rule"></div>

    <ul class="contacts">
      <li>
        <svg viewBox="0 0 24 24" aria-hidden="true"><path d="M3 9c0-3 4-5 9-5s9 2 9 5v1h-5V8H8v2H3z M6 11h12l2 9H4z"/></svg>
        417-555-0142
      </li>
      <li>
        <svg viewBox="0 0 24 24" aria-hidden="true"><path d="M7 3h10v5H7z M3 9h18v8h-4v4H7v-4H3z M9 14v5h6v-5z"/></svg>
        417-555-0187
      </li>
      <li>
        <svg viewBox="0 0 24 24" aria-hidden="true"><path d="M2 5h20v14H2z M4 7v1l8 5 8-5V7l-8 5z"/></svg>
        info@larkvalereview.com
      </li>
      <li>
        <svg viewBox="0 0 24 24" aria-hidden="true"><path d="M10 14l4-4 1.4 1.4-4 4z M7 12l-3 3a3 3 0 004 4l3-3-1.4-1.4-3 3a1 1 0 01-1.2-1.2l3-3z M17 12l3-3a3 3 0 00-4-4l-3 3 1.4 1.4 3-3a1 1 0 011.2 1.2l-3 3z"/></svg>
        www.larkvalereview.com
      </li>
    </ul>

    <div class="credential">
      <div class="credential-seal" role="img" aria-label="Certified home inspector membership seal"></div>
      <p class="credential-text">18 years Experience</p>
    </div>
  </section>

</main>
</body>
</html>
```